A reimagined website for a cross-border tax firm

There are two aspects to this project for Brindlemoor Tax Advisory:
1) I need a logo update to accommodate increasing focus and specialization in my business. The byline under the name “Brindlemoor Tax Advisory” needs to change:
ORIGINAL: TAX SUPPORT FOR PUBLIC ACCOUNTING FIRMS
REVISED: CROSS-BORDER TAX SERVICES • U.S. & CANADA
2) I need a website “refresh” (see current website at www.levyhelpdesk.example) based on this logo – a new vision for a website with greater clarity, focus and organization. It should represent a re-envisioning of the current approach, and not the wholesale abandonment of the style represented there. I need it to be creative, compelling and attention grabbing, but still professional. This should, at a minimum, update any places where the old name/logo is used, but I want the redesign to go beyond this to something more intuitive. I need high quality separate PNG files of the various logo styles for use in various documents, but HTML coding would be a helpful but not necessary addition.

Target Market(s)

People in need of cross-border tax services - Canada and US

Coding

Number of Pages Required

Requirements
Must have
• Greater crispness, sharpness - higher resolution
• A more compelling, organized approach - make the wording and images more accessible to the website user (especially the staff bios, which have scroll bars now)
Nice to have
• Replacement of stock image with a true image of the Halifax skyline
Should not have
• Deviate from colour pattern represented in website logo of blue/orange
• Deviate from existing logo except for word replacement

```html
<!DOCTYPE html>
<html lang="en">
<head>
<meta charset="utf-8">
<title>Brindlemoor Tax Advisory – Website Screens</title>
<link href="https://fonts.googleapis.com/css2?family=Ubuntu:ital,wght@0,400;0,500;0,700;1,400&display=swap" rel="stylesheet">
<style>
  :root{
    --page:#ffffff;
    --night:#0d1014;
    --gold:#c9962e;
    --orange:#f5a623;
    --white:#ffffff;
    --ink:#141c26;
    --muted:#c9ccd1;
    --navy-band:#3c5290;
    --sky-band:#3ba6e2;
    --sky-col:#2b93d6;
    --rust-band:#d4512a;
    --amber-band:#f3aa3c;
    --vcard:#c63d27;
    --send:#e2860f;
  }
  *{box-sizing:border-box;margin:0;padding:0}
  html,body{width:1200px;height:1000px;overflow:hidden;background:var(--page)}
  body{position:relative;font-family:"Ubuntu",sans-serif;color:var(--white)}

  .screen{position:absolute;width:480px;height:274px;overflow:hidden;background:var(--night)}
  .screen--home{left:109px;top:82px}
  .screen--firms{left:604px;top:82px}
  .screen--team{left:109px;top:368px}
  .screen--testimonials{left:604px;top:368px}
  .screen--individuals{left:109px;top:654px}
  .screen--contact{left:604px;top:654px}

  .backdrop{position:absolute;inset:0;background:
    radial-gradient(ellipse at 50% 0%,#2b333c 0%,transparent 60%),
    linear-gradient(160deg,#1d242c 0%,#0b0e12 45%,#151b21 100%)}

  .masthead{position:absolute;left:0;top:0;width:480px;height:84px}
  .brand{position:absolute;top:21px;left:0;width:480px;text-align:center;font-weight:500;font-size:11px;line-height:13px;color:var(--white)}

  .rule{position:absolute;left:85px;width:310px;height:1px;background:linear-gradient(90deg,transparent,var(--gold) 20%,var(--gold) 80%,transparent)}
  .rule--top{top:54px}
  .rule--bottom{top:74px}
  .flourish{position:absolute;left:224px;width:32px;height:6px;background:var(--gold);border-radius:3px;opacity:.9}
  .flourish--nav{top:51px}

  .nav{position:absolute;top:62px;left:0;width:480px;display:flex;justify-content:center;align-items:center;gap:9px;font-size:5.3px;list-style:none}
  .nav li{display:flex;align-items:center;gap:9px}
  .nav li + li::before{content:"";width:2.5px;height:2.5px;background:var(--gold);transform:rotate(45deg)}
  .nav .is-active{color:var(--orange)}

  .band{position:absolute;left:0;top:84px;width:480px;height:146px;overflow:hidden}
  .band__photo{position:absolute;inset:0}

  .footer{position:absolute;left:0;top:230px;width:480px;height:44px}
  .footer .rule{top:15px}
  .flourish--foot{top:12px}
  .copyright{position:absolute;top:31px;width:480px;text-align:center;font-size:4px;color:var(--muted)}

  .chevron{position:absolute;left:235px;top:127px;width:10px;height:7px}
  .copy{position:absolute;font-size:4.6px;line-height:6.4px}
  .copy p + p{margin-top:6px}
  .heading{font-weight:700;font-size:8.5px;line-height:10px;margin-bottom:8px;color:var(--ink)}

  /* home */
  .hero{background:linear-gradient(180deg,#d9ecf8 0%,#7fb8e4 35%,#1f5a96 75%,#0e2b52 100%)}
  .hero__towers{position:absolute;inset:0;background:
    linear-gradient(100deg,#0f2f57 0%,#1b4b82 26%,transparent 38%),
    linear-gradient(260deg,#0f2f57 0%,#1e5a95 30%,transparent 45%)}
  .hero__brand{position:absolute;left:0;top:64px;width:480px;text-align:center;font-weight:500;font-size:13px;color:var(--white)}
  .hero__arrow{position:absolute;top:68px;width:7px;height:10px}
  .hero__arrow--prev{left:18px}
  .hero__arrow--next{left:455px}

  /* firms */
  .firms-photo{background:linear-gradient(90deg,#48536a 0%,#3b4f8a 30%,#3d5392 70%,#4a566d 100%)}
  .firms-panel{position:absolute;left:85px;top:0;width:300px;height:146px;background:var(--navy-band);opacity:.9}
  .firms-copy{left:101px;top:20px;width:268px;font-size:4.4px;line-height:6px}
  .firms-copy .heading{margin-bottom:7px}

  /* team */
  .team-photo{background:linear-gradient(90deg,#57baf0 0%,var(--sky-band) 50%,#1f7dc6 100%)}
  .team-column{position:absolute;left:93px;top:0;width:167px;height:146px;background:var(--sky-col)}
  .team-copy{left:104px;top:26px;width:152px}
  .team-copy .heading{font-weight:500;font-size:9px;margin-bottom:11px}
  .team-portrait{position:absolute;left:276px;top:15px;width:90px;height:131px;background:linear-gradient(180deg,#3d7fb7 0%,#25313f 55%,#151a22 100%);border-radius:40px 40px 0 0}
  .team-next{position:absolute;left:358px;top:133px;font-size:3.8px;font-weight:700}

  /* testimonials */
  .rust-photo{background:linear-gradient(90deg,#cf4c27 0%,var(--rust-band) 50%,#c9502f 100%)}
  .quote-mark{position:absolute;font-family:Georgia,serif;font-size:34px;line-height:30px;color:#b23f1f}
  .quote-mark--open{left:69px;top:12px}
  .quote-mark--close{left:374px;top:114px}
  .testimonials-title{position:absolute;left:102px;top:16px;font-weight:700;font-size:8.5px;color:var(--ink)}
  .review{position:absolute;left:104px;width:262px;display:flex;gap:19px}
  .review--one{top:35px}
  .review--two{top:85px}
  .review__avatar{flex:none;width:29px;height:29px;border:1.5px solid #f1d6c8;background:linear-gradient(180deg,#e9c9b6,#b9856b)}
  .review__name{font-weight:700;font-size:5px;line-height:7px;margin-top:2px;color:var(--ink)}
  .review__text{font-style:italic;font-size:4.3px;line-height:6px}
  .review-divider{position:absolute;left:104px;top:78px;width:270px;height:1px;background:rgba(255,255,255,.35)}

  /* individuals */
  .amber-photo{background:linear-gradient(90deg,#f0a334 0%,var(--amber-band) 45%,#f5b552 100%)}
  .individuals-copy{left:102px;top:20px;width:266px}
  .individuals-copy ul{list-style:none;margin-top:6px}
  .individuals-copy li{display:flex;gap:5px;line-height:7px}
  .individuals-copy li::before{content:"›";font-weight:700}

  /* contact */
  .contact-title{position:absolute;top:108px;font-size:8px;color:var(--orange)}
  .contact-info{left:101px;width:140px}
  .contact-form{left:243px}
  .contact-list{position:absolute;left:101px;top:127px;list-style:none;font-size:4.6px;line-height:6px}
  .contact-list li{display:flex;align-items:center;gap:6px;height:12.5px}
  .contact-list li.indent{padding-left:13px}
  .contact-list svg{width:6px;height:6px}
  .btn{position:absolute;display:flex;align-items:center;justify-content:center;font-size:5px;font-weight:700;color:var(--white)}
  .btn--vcard{left:102px;top:191px;width:88px;height:12px;background:var(--vcard)}
  .btn--send{left:243px;top:191px;width:66px;height:12px;background:var(--send)}
  .field{position:absolute;background:var(--white);color:#9aa0a6;font-size:4px;padding:3px 3px}
  .field--name{left:243px;top:126px;width:66px;height:12px}
  .field--phone{left:313px;top:126px;width:66px;height:12px}
  .field--email{left:243px;top:142px;width:136px;height:12px}
  .field--message{left:243px;top:158px;width:136px;height:29px}
</style>
</head>
<body>

<!-- Home -->
<section class="screen screen--home">
  <div class="backdrop" role="img" aria-label="Dark photo of city towers at night"></div>
  <header class="masthead">
    <div class="brand">Brindlemoor Tax Advisory</div>
    <div class="rule rule--top"></div><div class="flourish flourish--nav" role="img" aria-label="Gold flourish ornament"></div>
    <ul class="nav"><li class="is-active">Home</li><li>Our Team</li><li>For Individuals</li><li>For Public Accounting Firms</li><li>Testimonials</li><li>Contact</li></ul>
    <div class="rule rule--bottom"></div>
  </header>
  <div class="band hero" role="img" aria-label="Photo looking up at glass office towers against a bright sky">
    <div class="hero__towers"></div>
    <div class="hero__brand">Brindlemoor Tax Advisory</div>
    <svg class="hero__arrow hero__arrow--prev" viewBox="0 0 7 10"><path d="M6 1 2 5l4 4" fill="none" stroke="#fff" stroke-width="1.4"/></svg>
    <svg class="hero__arrow hero__arrow--next" viewBox="0 0 7 10"><path d="M1 1l4 4-4 4" fill="none" stroke="#fff" stroke-width="1.4"/></svg>
  </div>
  <footer class="footer"><div class="rule"></div><div class="flourish flourish--foot" role="img" aria-label="Gold flourish ornament"></div><p class="copyright">Copyright © 2016 Brindlemoor Tax Advisory Inc.</p></footer>
</section>

<!-- For Public Accounting Firms -->
<section class="screen screen--firms">
  <div class="backdrop" role="img" aria-label="Dark photo of city towers at night"></div>
  <header class="masthead">
    <div class="brand">Brindlemoor Tax Advisory</div>
    <div class="rule rule--top"></div><div class="flourish flourish--nav" role="img" aria-label="Gold flourish ornament"></div>
    <ul class="nav"><li>Home</li><li>Our Team</li><li>For Individuals</li><li class="is-active">For Public Accounting Firms</li><li>Testimonials</li><li>Contact</li></ul>
    <div class="rule rule--bottom"></div>
  </header>
  <div class="band">
    <div class="band__photo firms-photo" role="img" aria-label="Blue-tinted photo of an open office"></div>
    <div class="firms-panel"></div>
    <div class="copy firms-copy">
      <h2 class="heading">For Public Accounting Firms</h2>
      <p>My core business is providing tax support for public accounting firms. Whatever the size of your firm and the need you have, I can help you.</p>
      <p>In large firms with established tax groups, I can fill the gap that often exists between partners and junior staff. In firms with only inexperienced tax staff, I can mentor, train and provide project management and quality control. And for small firms with only a periodic need for tax support, I can provide a full range of services - research, assistance with unusual or complex compliance and the selling/execution of special tax projects.</p>
      <p>I have a wide range of experience - rural and urban, Canadian and US, compliance and planning.</p>
      <p>I've been doing this for years and have a solid track record in providing tax support for public accounting firms (see my Proflink profile for further details on my work history). Call me to discuss how I can ease your workload.</p>
    </div>
    <svg class="chevron" viewBox="0 0 10 7"><path d="M1 1l4 4 4-4" fill="none" stroke="#fff" stroke-width="1.4"/></svg>
  </div>
  <footer class="footer"><div class="rule"></div><div class="flourish flourish--foot" role="img" aria-label="Gold flourish ornament"></div><p class="copyright">Copyright © 2016 Brindlemoor Tax Advisory Inc.</p></footer>
</section>

<!-- Our Team -->
<section class="screen screen--team">
  <div class="backdrop" role="img" aria-label="Dark photo of city towers at night"></div>
  <header class="masthead">
    <div class="brand">Brindlemoor Tax Advisory</div>
    <div class="rule rule--top"></div><div class="flourish flourish--nav" role="img" aria-label="Gold flourish ornament"></div>
    <ul class="nav"><li>Home</li><li class="is-active">Our Team</li><li>For Individuals</li><li>For Public Accounting Firms</li><li>Testimonials</li><li>Contact</li></ul>
    <div class="rule rule--bottom"></div>
  </header>
  <div class="band">
    <div class="band__photo team-photo" role="img" aria-label="Blue-tinted photo of a bright office"></div>
    <div class="team-column"></div>
    <div class="copy team-copy">
      <h2 class="heading">Owen R. Tallis, CGA</h2>
      <p>I've been practising tax now for 15 years. I began in a large firm environment (Harrow Kent LLP), where I spent most of my time on US personal and Canadian corporate compliance. After moving to Nova Scotia to work for Pellman Rowe LLP, my focus shifted to owner-managed businesses. I've seen it all - special tax projects of all kinds, personal, corporate and trust compliance (including U.S.) and issues surrounding immigration, emigration and non-residency. If I don't know the answer, I'll research it for you.</p>
    </div>
    <div class="team-portrait" role="img" aria-label="Portrait photo of the tax advisor in a dark suit, arms folded"></div>
    <span class="team-next">NEXT &gt;&gt;</span>
    <svg class="chevron" viewBox="0 0 10 7"><path d="M1 1l4 4 4-4" fill="none" stroke="#fff" stroke-width="1.4"/></svg>
  </div>
  <footer class="footer"><div class="rule"></div><div class="flourish flourish--foot" role="img" aria-label="Gold flourish ornament"></div><p class="copyright">Copyright © 2016 Brindlemoor Tax Advisory Inc.</p></footer>
</section>

<!-- Testimonials -->
<section class="screen screen--testimonials">
  <div class="backdrop" role="img" aria-label="Dark photo of city towers at night"></div>
  <header class="masthead">
    <div class="brand">Brindlemoor Tax Advisory</div>
    <div class="rule rule--top"></div><div class="flourish flourish--nav" role="img" aria-label="Gold flourish ornament"></div>
    <ul class="nav"><li>Home</li><li>Our Team</li><li>For Individuals</li><li>For Public Accounting Firms</li><li class="is-active">Testimonials</li><li>Contact</li></ul>
    <div class="rule rule--bottom"></div>
  </header>
  <div class="band">
    <div class="band__photo rust-photo" role="img" aria-label="Orange-tinted photo of a business meeting"></div>
    <span class="quote-mark quote-mark--open">“</span>
    <span class="quote-mark quote-mark--close">”</span>
    <h2 class="testimonials-title">Testimonials</h2>
    <article class="review review--one">
      <div class="review__avatar" role="img" aria-label="Client portrait photo"></div>
      <div><p class="review__name">Carl Whitby</p><p class="review__text">Fusce suscipit varius mi. Cum sociis natoque penatibus et magnis dis parturient montes, nascetur ridiculus mus. Nulla dui. Fusce feugiat malesuada odio. Morbi nunc odio, gravida at, cursus nec, luctus a, lorem.</p></div>
    </article>
    <div class="review-divider"></div>
    <article class="review review--two">
      <div class="review__avatar" role="img" aria-label="Client portrait photo"></div>
      <div><p class="review__name">Carl Whitby</p><p class="review__text">Fusce suscipit varius mi. Cum sociis natoque penatibus et magnis dis parturient montes, nascetur ridiculus mus. Nulla dui. Fusce feugiat malesuada odio. Morbi nunc odio, gravida at, cursus nec, luctus a, lorem.</p></div>
    </article>
    <svg class="chevron" viewBox="0 0 10 7"><path d="M1 1l4 4 4-4" fill="none" stroke="#fff" stroke-width="1.4"/></svg>
  </div>
  <footer class="footer"><div class="rule"></div><div class="flourish flourish--foot" role="img" aria-label="Gold flourish ornament"></div><p class="copyright">Copyright © 2016 Brindlemoor Tax Advisory Inc.</p></footer>
</section>

<!-- For Individuals -->
<section class="screen screen--individuals">
  <div class="backdrop" role="img" aria-label="Dark photo of city towers at night"></div>
  <header class="masthead">
    <div class="brand">Brindlemoor Tax Advisory</div>
    <div class="rule rule--top"></div><div class="flourish flourish--nav" role="img" aria-label="Gold flourish ornament"></div>
    <ul class="nav"><li>Home</li><li>Our Team</li><li class="is-active">For Individuals</li><li>For Public Accounting Firms</li><li>Testimonials</li><li>Contact</li></ul>
    <div class="rule rule--bottom"></div>
  </header>
  <div class="band">
    <div class="band__photo amber-photo" role="img" aria-label="Amber-tinted photo of two people reviewing documents"></div>
    <div class="copy individuals-copy">
      <h2 class="heading">For Individuals</h2>
      <p>If you are an individual in need of tax support, I may be able to help you.</p>
      <p>First, let me describe what I don't do. I don't do bookkeeping or accounting. So if you are running a business and you need what accountants call "year end" services (that is, having an accountant check your bookkeeping, draft financial statements and prepare the corresponding tax returns), you really need a public accountant. I can refer you to some good firms if you don't know of any.</p>
      <p>My focus is on more specialized and non-typical tax work. The following list will give you an idea of the areas I practice in:</p>
      <ul><li>Complex Canadian personal tax filings (especially involving foreign income or unusual situations)</li><li>US personal tax filings</li></ul>
    </div>
    <svg class="chevron" viewBox="0 0 10 7"><path d="M1 1l4 4 4-4" fill="none" stroke="#fff" stroke-width="1.4"/></svg>
  </div>
  <footer class="footer"><div class="rule"></div><div class="flourish flourish--foot" role="img" aria-label="Gold flourish ornament"></div><p class="copyright">Copyright © 2016 Brindlemoor Tax Advisory Inc.</p></footer>
</section>

<!-- Contact -->
<section class="screen screen--contact">
  <div class="backdrop" role="img" aria-label="Dark photo of city towers at night"></div>
  <header class="masthead">
    <div class="brand">Brindlemoor Tax Advisory</div>
    <div class="rule rule--top"></div><div class="flourish flourish--nav" role="img" aria-label="Gold flourish ornament"></div>
    <ul class="nav"><li>Home</li><li>Our Team</li><li>For Individuals</li><li>For Public Accounting Firms</li><li>Testimonials</li><li class="is-active">Contact</li></ul>
    <div class="rule rule--bottom"></div>
  </header>
  <h2 class="contact-title contact-info">Contact Information</h2>
  <ul class="contact-list">
    <li><svg viewBox="0 0 6 6"><path d="M3 6C1.5 4 1 3.2 1 2.2a2 2 0 0 1 4 0C5 3.2 4.5 4 3 6z" fill="#f5a623"/><circle cx="3" cy="2.2" r=".7" fill="#0d1014"/></svg>418 Quarry Lane, Unit 9</li>
    <li class="indent">Eastvale, Nova Scotia, Canada B0X 2Q4</li>
    <li><svg viewBox="0 0 6 6"><path d="M1.2.5 2.3 1.8 1.7 2.6Q2.6 4 3.6 4.4l.8-.6L5.6 5 4.8 5.8Q2.6 5.6.4 1.4z" fill="#f5a623"/></svg>Phone: (555) 014-2291</li>
    <li><svg viewBox="0 0 6 6"><rect x="1.5" y=".5" width="3" height="1.8" fill="#f5a623"/><rect x=".5" y="2.3" width="5" height="2.4" rx=".4" fill="#f5a623"/><rect x="1.5" y="4" width="3" height="1.6" fill="#f5a623"/></svg>Fax: (555) 014-2292</li>
  </ul>
  <div class="btn btn--vcard">Download Vcard</div>
  <h2 class="contact-title contact-form">Send Us A Message</h2>
  <div class="field field--name">Name</div>
  <div class="field field--phone">Phone</div>
  <div class="field field--email">Email Address</div>
  <div class="field field--message">Message</div>
  <div class="btn btn--send">Send</div>
  <footer class="footer"><div class="rule"></div><div class="flourish flourish--foot" role="img" aria-label="Gold flourish ornament"></div><p class="copyright">Copyright © 2016 Brindlemoor Tax Advisory Inc.</p></footer>
</section>

</body>
</html>
```